K7Q480 brochure

We want a new brochure for our rebranding of our sports health and wellness centre. We are based in Townsville in North Queensland. We provide chiropractic, physiotherapy, massage, nutrition and yoga services. We would like to see designs and content that portray our unique one stop destination for many allied health services and our one on one functional rehab approach customised to each individual. We would like to keep colours that compliment our logo colours. The design should be professional and one that could be handed out to Medical Doctors, other referring healthcare professionals and prospective sports and active lifestyle patients. The brochure should also note that we also accept/treat Labormend, RSF, Healthwell TCP, and Accident and Injury referrals
Updates

Please check out our website for more information on who we are and what we do. I will upload our new logo in a few moments. Cheers! Www.corelift-vexa.com.au

Project Deadline Extended
Reason: We understand creating a quality brochure takes time and we wanted to give the creatives more time to create. With the extended deadline we are now guaranteeing the payment.

Target Market(s)

Referring Medical Doctors and other health professionals
Athletes and Active lifestyle patients
Wellness patients

Industry/Entity Type

Healthcare

Requirements
Nice to have
• Brochure can be single double sided, or bi-fold of approx. size of 210mm x 99mm
Should not have
• Brochure should not focus on or place emphasis on one particular service that we offer rather focus on the services provided as a whole.

```html
<!DOCTYPE html>
<html lang="en">
<head>
<meta charset="utf-8">
<title>K7Q480 Brochure</title>
<link rel="stylesheet" href="https://fonts.googleapis.com/css2?family=Roboto+Condensed:wght@400;700;900&display=swap">
<style>
  :root {
    --page: #ffffff;
    --brand-red: #e31c24;
    --brand-blue: #0a3f8c;
    --ink-light: #ffffff;
  }
  * { margin: 0; padding: 0; box-sizing: border-box; }
  html, body {
    width: 848px; height: 1200px; overflow: hidden;
    background: var(--page);
    font-family: "Roboto Condensed", "Arial Narrow", sans-serif;
  }
  .canvas { position: relative; width: 848px; height: 1200px; }
  .panel {
    position: absolute; left: 224px; top: 176px;
    width: 400px; height: 848px; overflow: hidden;
    background: var(--brand-red);
  }
  .panel-shapes { position: absolute; inset: 0; }
  .athlete-photo {
    position: absolute; left: 40px; top: 0; width: 320px; height: 848px;
    background: radial-gradient(ellipse 45% 55% at 50% 45%, rgba(26,16,20,0.78), rgba(26,16,20,0.35) 70%, rgba(26,16,20,0) 100%);
  }
  .brand {
    position: absolute; left: 0; top: 62px; width: 400px;
    display: flex; flex-direction: column; align-items: center;
    color: var(--ink-light);
  }
  .brand-row { display: flex; align-items: center; gap: 12px; }
  .brand-dot { width: 34px; height: 34px; border-radius: 50%; background: var(--ink-light); }
  .brand-name { font-weight: 700; font-size: 38px; line-height: 1; letter-spacing: 1px; }
  .brand-tagline { font-weight: 700; font-size: 13px; letter-spacing: 1px; margin-top: 4px; }
  .headline {
    position: absolute; left: 0; width: 400px;
    color: var(--ink-light); font-weight: 900;
    white-space: nowrap; text-align: center;
    transform: rotate(-8deg); transform-origin: center;
  }
  .headline-top { top: 156px; font-size: 60px; }
  .headline-mid { top: 234px; font-size: 40px; }
  .headline-main { top: 294px; font-size: 70px; }
  .services {
    position: absolute; left: 0; top: 448px; width: 400px;
    color: var(--ink-light); text-align: center;
    transform: rotate(-5deg); transform-origin: center;
  }
  .services-intro { font-size: 26px; margin-bottom: 10px; }
  .services-list { list-style: none; font-size: 36px; line-height: 40px; }
  .referrals {
    position: absolute; left: 30px; top: 758px; width: 340px;
    color: var(--ink-light); text-align: center;
    font-size: 15px; line-height: 19px;
  }
  .referrals strong { font-weight: 700; }
  .website {
    position: absolute; left: 0; bottom: 18px; width: 400px;
    text-align: center; color: var(--ink-light); font-size: 23px;
  }
</style>
</head>
<body>
<main class="canvas">
  <section class="panel">
    <svg class="panel-shapes" width="400" height="848" viewBox="0 0 400 848" aria-hidden="true">
      <polygon points="0,220 400,134 400,664 0,746" fill="var(--brand-blue)"/>
      <polygon points="0,282 400,198 400,204 0,288" fill="var(--brand-red)"/>
      <polygon points="0,346 400,262 400,268 0,352" fill="var(--brand-red)"/>
      <polygon points="0,438 400,354 400,366 0,450" fill="var(--brand-red)"/>
    </svg>
    <div class="athlete-photo" role="img" aria-label="Photo of an athlete running toward the viewer, dark silhouette"></div>

    <header class="brand">
      <div class="brand-row">
        <span class="brand-dot"></span>
        <span class="brand-name">K7Q480</span>
      </div>
      <span class="brand-tagline">Sports Health and Wellness</span>
    </header>

    <h1>
      <span class="headline headline-top">Improve Your</span>
      <span class="headline headline-mid">Wellness With Our</span>
      <span class="headline headline-main">Expert Team</span>
    </h1>

    <div class="services">
      <p class="services-intro">Proudly Providing :</p>
      <ul class="services-list">
        <li>Chiropractic</li>
        <li>Physiotherapy</li>
        <li>Massage</li>
        <li>Nutrition</li>
        <li>Yoga</li>
      </ul>
    </div>

    <p class="referrals">We accept <strong>Labormend, RSF, Healthwell TCP</strong><br>and Accident &amp; Injury referrals</p>

    <p class="website">www.corelift-vexa.com.au</p>
  </section>
</main>
</body>
</html>
```